Letterhead Design Project

Our firm recently came out with a new logo and new website and we would like to design letterhead that makes use of the new look.

Our firm is an energy consulting firm. We help our customers find ways to spend less money on their energy expenses (we cater to commercial and industrial accounts) by helping them find a lower rate for every unit of energy they consume, install more energy efficient measures so that they end up using fewer units of energy or determine if making the energy themselves can be done more cost effectively

Industry/Entity Type

Industrial

Requirements
Must have
• Must have our logo
must have our contact information
Nice to have
• some sort of watermark

```html
<!DOCTYPE html>
<html lang="en">
<head>
<meta charset="utf-8">
<title>Halden Energy Letterhead</title>
<link rel="stylesheet" href="https://fonts.googleapis.com/css2?family=Montserrat:wght@400;500&display=swap">
<style>
  :root {
    --band-teal: #3db5c2;
    --ink-dark: #3b4045;
    --ink-muted: #8a9096;
    --paper: #ffffff;
    --on-band: #ffffff;
  }
  html, body {
    margin: 0;
    padding: 0;
    width: 874px;
    height: 1200px;
    overflow: hidden;
    background: var(--paper);
  }
  .letterhead {
    position: relative;
    width: 874px;
    height: 1200px;
    background: var(--paper);
    font-family: "Montserrat", sans-serif;
  }
  .side-band {
    position: absolute;
    left: 0;
    top: 0;
    width: 200px;
    height: 1200px;
    background: var(--band-teal);
  }
  .contact-block {
    position: absolute;
    top: 46px;
    left: 28px;
    writing-mode: vertical-rl;
    color: var(--on-band);
    font-size: 13px;
    line-height: 19px;
    letter-spacing: 0.3px;
    margin: 0;
    font-style: normal;
  }
  .brand {
    position: absolute;
    top: 80px;
    right: 40px;
    display: flex;
    align-items: center;
    gap: 14px;
  }
  .brand-mark {
    width: 30px;
    height: 30px;
    background: var(--ink-dark);
  }
  .brand-name {
    font-size: 34px;
    font-weight: 400;
    letter-spacing: 7px;
    color: var(--ink-dark);
    line-height: 1;
  }
  .site-address {
    position: absolute;
    left: 200px;
    right: 0;
    bottom: 20px;
    text-align: center;
    font-size: 11px;
    letter-spacing: 0.4px;
    color: var(--ink-muted);
  }
</style>
</head>
<body>
  <main class="letterhead">
    <aside class="side-band">
      <address class="contact-block">
        <span>1420 Marlow Ave</span><br>
        <span>Fresno, CA</span><br>
        <span>93711-2205</span><br>
        <span>(559) 555-0142</span>
      </address>
    </aside>
    <header class="brand">
      <span class="brand-mark"></span>
      <span class="brand-name">HALDEN ENERGY</span>
    </header>
    <footer class="site-address">www.haldenenergy.com</footer>
  </main>
</body>
</html>
```